Junk Removal Website Design

We are working with a Junk Removal company in California. They provide junk hauling services for commercial and residential throughout California.
Some sites to use for inspiration:
https://www.1877binclear.com
https://haulwaycleanoutpro.com
https://www.quarrybrawnmovingclutter.com
https://www.clutterliftwardens.com
Thank you for taking the time to consider designing a website for us. We are web developers based in Stockton, CA, USA. Most of our projects go through the same process. Understanding this process may help you win a project with us. We custom-code all of our websites in-house. We don’t have any requirements as to what tools you use for your design, but we ask that you follow these guidelines.
IMAGES:
If you use any images or icons in the design, we ask that you have a link to the asset so we can purchase the image/icon. Most of the designs we submit do not have the customer’s images on them unless they have some great images. Be creative; show us the feeling you are trying to portray with your image choices. Use any royalty-free site you choose. We subscribe to Vexaro and mainly use their images, but we can purchase images outside of Vexaro. PLEASE NOTE: we will not submit designs to clients with watermarks on the images.
FONTS:
We ask that you identify the fonts you’re using in the design. This can be done in a message if you want. We typically use Plimbet Fonts and Vexaro Fonts.
CONTENT:
We're always open to different content and ideas. We often submit designs with stock images so the client can see our vision. We typically take pictures after the website launch to use their images with our vision. Lorem Ipsum is fine for paragraphs, but we ask that you make the Headers with correct English. We want to be able to show the vision and identify the sections of the website.
INSPIRATION:
We typically add a couple of links in the brief of websites we like to help you get started in your design.
REVISIONS:
We do not often ask for revisions of the designs unless we see something in the design that may not appeal to the client. If there are slight changes that we want to make, we do that in the development process.
FEEDBACK:
We rarely give feedback on designs during the design process. We are working on many website projects and do not have the time to provide feedback. We usually respond if your request is well thought out and asks specific questions, but a note asking “feedback, please” usually goes unanswered.
Number of Pages Required
1 page

```html
<!DOCTYPE html>
<html lang="en">
<head>
<meta charset="utf-8">
<title>Haulbright – Junk Removal</title>
<link href="https://fonts.googleapis.com/css2?family=Bowlby+One&family=Poppins:wght@400;500;600;700&display=swap" rel="stylesheet">
<style>
:root{
  --green:#4ea340;
  --green-dark:#3d8a31;
  --mint:#eef6ec;
  --ink:#1e1e1e;
  --dark:#2b2929;
  --grey:#555;
  --white:#fff;
}
*{margin:0;padding:0;box-sizing:border-box}
html,body{width:1200px;height:4565px;overflow:hidden}
body{position:relative;background:var(--white);font-family:"Poppins",sans-serif;color:var(--ink)}
.abs{position:absolute}
.display{font-family:"Bowlby One",sans-serif;text-transform:uppercase;line-height:1.02;color:var(--ink)}
.display em{font-style:normal;color:var(--green)}
.body-copy{font-size:12.5px;line-height:27px;color:var(--grey)}
.btn{position:absolute;display:flex;align-items:center;justify-content:center;font-size:11px;font-weight:700;text-transform:uppercase;color:var(--white);border-radius:5px;box-shadow:0 8px 16px rgba(0,0,0,.18)}
.btn.green{background:var(--green)}
.btn.black{background:var(--ink)}
.photo{position:absolute;border-radius:50%;overflow:hidden}
.brand{font-family:"Bowlby One",sans-serif;text-transform:uppercase;color:var(--ink);letter-spacing:1px}

/* header */
.topbar{left:348px;top:0;width:852px;height:52px;background:var(--green);color:var(--white);font-size:10.5px}
.topbar .item{position:absolute;top:14px;display:flex;align-items:center;gap:14px}
.topbar .dot{width:24px;height:24px;border-radius:50%;background:var(--white);display:flex;align-items:center;justify-content:center}
.search{position:absolute;left:524px;top:12px;width:192px;height:28px;border:1.5px solid var(--white);border-radius:14px;padding:6px 22px;font-size:10px}
.nav{left:425px;top:78px;display:flex;gap:50px;font-size:10px;text-transform:uppercase}
.nav .active{font-weight:700}

/* hero */
.hero{left:0;top:120px;width:1200px;height:540px;background:linear-gradient(90deg,#eaf4e7,#fafdf9 60%,#fff)}
.eyebrow{font-size:10px;font-weight:600;color:var(--green);text-transform:uppercase}
.zip-card{left:92px;top:680px;width:480px;height:287px;background:var(--mint);box-shadow:0 10px 30px rgba(0,0,0,.07);border-radius:6px}
.zip-input{left:53px;top:135px;width:370px;height:36px;background:var(--white);border-radius:4px;box-shadow:0 4px 10px rgba(0,0,0,.08);font-size:11px;color:#999;padding:10px 36px}
.faint-brand{color:#edf4ec}

/* services */
.services{left:0;top:1692px;width:1200px;height:722px;background:var(--mint)}
.arrow-btn{position:absolute;width:38px;height:38px;border-radius:50%;display:flex;align-items:center;justify-content:center}

/* expert */
.tag{position:absolute;height:36px;width:124px;background:var(--ink);color:var(--white);font-family:"Bowlby One",sans-serif;font-size:12px;display:flex;align-items:center;justify-content:center;border-radius:5px}

/* testimonials */
.testimonials{left:0;top:3305px;width:1200px;height:633px;background:var(--dark)}
.card{position:absolute;top:247px;width:450px;height:217px;background:var(--green);color:var(--white)}
.card .avatar{position:absolute;left:28px;top:24px;width:74px;height:74px;border-radius:50%;background:linear-gradient(135deg,#f3d3bb,#d9a27e);border:3px solid var(--white)}
.card p{position:absolute;left:133px;top:60px;width:290px;font-size:11.5px;line-height:21px}
.card .name{position:absolute;left:133px;top:170px;font-family:"Bowlby One",sans-serif;font-size:12px}
.card .role{position:absolute;left:133px;top:188px;font-size:9.5px}
.quote{position:absolute;left:133px;top:28px;font-family:"Bowlby One",sans-serif;font-size:30px;line-height:1}

/* footer */
.foot-col h3{font-family:"Bowlby One",sans-serif;font-size:24px;text-transform:uppercase;margin-bottom:22px}
.foot-links{font-size:11.5px;line-height:27px;list-style:none}
.contact-row{display:flex;align-items:center;gap:22px;font-size:11.5px;margin-bottom:28px}
.contact-row .dot{width:32px;height:32px;border-radius:50%;background:var(--green);flex:none;display:flex;align-items:center;justify-content:center}
.social{display:flex;gap:22px;margin-top:18px}
.social span{width:18px;height:18px;border-radius:50%;background:var(--green)}
.divider{width:2px;height:170px;background:#bbb}
</style>
</head>
<body>

<!-- Header -->
<div class="abs brand" style="left:118px;top:22px;font-size:30px;color:var(--green);line-height:1">Haulbright</div>
<div class="abs brand" style="left:118px;top:58px;font-size:19px;line-height:1">Junk Removal</div>

<div class="abs topbar">
  <div class="item" style="left:75px"><span class="dot"><svg width="12" height="12" viewBox="0 0 24 24"><path fill="#4ea340" d="M6.6 10.8a15 15 0 006.6 6.6l2.2-2.2c.3-.3.7-.4 1-.2 1.1.4 2.3.6 3.6.6.6 0 1 .4 1 1V20c0 .6-.4 1-1 1A17 17 0 013 4c0-.6.4-1 1-1h3.5c.6 0 1 .4 1 1 0 1.3.2 2.5.6 3.6.1.3 0 .7-.2 1z"/></svg></span>555-014-7730</div>
  <div class="item" style="left:277px"><span class="dot"><svg width="12" height="10" viewBox="0 0 24 18"><path fill="#4ea340" d="M0 0h24v18H0z"/><path d="M1 1l11 8 11-8" stroke="#fff" stroke-width="2" fill="none"/></svg></span>hello@haulbright.com</div>
  <div class="search">Search
    <svg class="abs" style="right:14px;top:7px" width="11" height="11" viewBox="0 0 24 24"><circle cx="10" cy="10" r="7" stroke="#fff" stroke-width="3" fill="none"/><path d="M15 15l7 7" stroke="#fff" stroke-width="3"/></svg>
  </div>
</div>
<div class="abs nav"><span class="active">Home</span><span>Who We Are</span><span>What We Remove</span><span>Jobs We Do</span><span>Our Work</span><span>Blog</span><span>FAQ</span></div>

<!-- Hero -->
<div class="abs hero"></div>
<div class="abs" style="left:34px;top:205px;width:1px;height:155px;background:#bbb"></div>
<div class="abs" style="left:34px;top:450px;width:1px;height:150px;background:#bbb"></div>
<svg class="abs" style="left:23px;top:385px" width="22" height="34" viewBox="0 0 22 34"><rect x="1" y="1" width="20" height="32" rx="10" fill="#4ea340"/><rect x="10" y="7" width="2" height="8" fill="#fff"/></svg>
<div class="abs eyebrow" style="left:135px;top:251px">Don't let junk pile up, call us to clean it up.</div>
<h1 class="abs display" style="left:135px;top:275px;font-size:49px">Let us handle<br>your <em>junk</em><br>removal needs.</h1>
<div class="btn green" style="left:135px;top:478px;width:165px;height:36px">Contact us</div>

<div class="photo" role="img" aria-label="Worker in hard hat and safety vest beside a green garbage truck and wheelie bins" style="left:603px;top:124px;width:604px;height:604px;background:linear-gradient(135deg,#4b7a2e,#6db84a 40%,#8f7f55 70%,#d8c93a)"></div>
<svg class="abs" style="left:560px;top:110px" width="660" height="620" viewBox="0 0 660 620">
  <path d="M80 330 A305 305 0 0 0 640 480" stroke="#4ea340" stroke-width="2.5" fill="none"/>
  <circle cx="68" cy="345" r="26" fill="#fff" stroke="#4ea340" stroke-width="1.5"/>
  <text x="68" y="353" text-anchor="middle" font-family="Bowlby One,sans-serif" font-size="18" fill="#4ea340">01</text>
  <circle cx="68" cy="420" r="5" fill="#fff" stroke="#4ea340" stroke-width="2"/>
  <circle cx="88" cy="460" r="5" fill="#4ea340"/><circle cx="108" cy="487" r="5" fill="#4ea340"/><circle cx="138" cy="516" r="5" fill="#4ea340"/>
</svg>

<!-- Zip card -->
<div class="abs zip-card">
  <h2 class="abs display" style="left:53px;top:40px;font-size:25px">Tell our <em>team</em> what you<br>want gone!</h2>
  <div class="abs zip-input">Enter Zip Code</div>
  <div class="btn black" style="left:53px;top:207px;width:212px;height:36px">Check availability</div>
</div>
<div class="abs brand faint-brand" style="left:700px;top:820px;font-size:102px;line-height:.9">Haul<br><span style="font-size:58px">Bright</span></div>

<!-- Moving -->
<div class="photo" role="img" aria-label="Large teal and orange commercial waste bins" style="left:102px;top:1101px;width:496px;height:496px;background:linear-gradient(120deg,#ff7a1a 0%,#1aa889 35%,#23c3a0 60%,#1e4fd8 100%);box-shadow:-8px 14px 0 #e8f1e6"></div>
<h2 class="abs display" style="left:639px;top:1163px;font-size:50px">Moving what<br><em>you</em> want</h2>
<p class="abs body-copy" style="left:639px;top:1288px;width:440px">Lorem Ipsum is simply dummy text of the printing and typesetting industry. Lorem Ipsum has been the industry's standard dummy text ever since the 1500s, when an unknown printer took a galley of type and scrambled it to make a type specimen book. It has survived not only five centuries, but also the leap into electronic typesetting, remaining essentially unchanged.</p>
<div class="btn green" style="left:639px;top:1480px;width:165px;height:36px">Read more</div>

<!-- Services -->
<div class="abs services"></div>
<h2 class="abs display" style="left:135px;top:1778px;font-size:50px">Our <em>removal</em><br>services</h2>
<p class="abs body-copy" style="left:135px;top:1903px;width:365px">Lorem Ipsum is simply dummy text of the printing and typesetting industry. Lorem Ipsum has been the industry's standard dummy text ever since the 1500s, when an unknown printer took a galley of type and scrambled it to make a type specimen book. It has survived not only five centuries, but also the leap into electronic typesetting, remaining essentially unchanged.</p>
<p class="abs body-copy" style="left:135px;top:2118px;width:365px">Lorem Ipsum is simply dummy text of the printing and typesetting industry.</p>
<div class="btn black" style="left:135px;top:2204px;width:165px;height:36px">Learn more</div>
<div class="arrow-btn" style="left:135px;top:2294px;background:#fff"><svg width="22" height="10" viewBox="0 0 22 10"><path d="M22 5H2M6 1L2 5l4 4" stroke="#222" stroke-width="1.5" fill="none"/></svg></div>
<div class="arrow-btn" style="left:203px;top:2294px;background:var(--green)"><svg width="22" height="10" viewBox="0 0 22 10"><path d="M0 5h20M16 1l4 4-4 4" stroke="#222" stroke-width="1.5" fill="none"/></svg></div>
<div class="photo" role="img" aria-label="Residential garage with rubbish bins in the snow" style="left:550px;top:1824px;width:466px;height:466px;background:linear-gradient(180deg,#c9b79a,#a99676 55%,#e8ecef 80%,#3a64b8)"></div>
<div class="abs display" style="left:690px;top:2022px;width:180px;text-align:center;font-size:20px;color:var(--green)">Residential<br>cleaning</div>
<svg class="abs" style="left:753px;top:2086px" width="60" height="12" viewBox="0 0 60 12"><path d="M0 6h56M50 1l6 5-6 5" stroke="#222" stroke-width="1.5" fill="none"/></svg>
<div class="photo" role="img" aria-label="Worker at a landfill site" style="left:1037px;top:2018px;width:78px;height:78px;background:linear-gradient(135deg,#9fb7c9,#7d8f5e)"></div>

<!-- Expert -->
<div class="abs brand" style="left:823px;top:2445px;font-size:64px;line-height:.9;color:#eef3ed">Haul<br><span style="font-size:36px">Bright</span></div>
<div class="tag" style="left:213px;top:2593px">Load it</div>
<div class="photo" role="img" aria-label="Workers loading waste into a garbage truck" style="left:334px;top:2481px;width:256px;height:256px;background:linear-gradient(180deg,#5f8a4a,#3a4f6a 50%,#2f7fb0)"></div>
<div class="photo" role="img" aria-label="Worker with bins beside a green truck" style="left:129px;top:2721px;width:256px;height:256px;background:linear-gradient(135deg,#3f9a2d,#8dbb3f 60%,#e0cf2c)"></div>
<div class="tag" style="left:388px;top:2829px">Haul it</div>
<div class="tag" style="left:208px;top:3067px">Dump it</div>
<div class="photo" role="img" aria-label="Excavator working on a landfill pile" style="left:334px;top:2957px;width:256px;height:256px;background:linear-gradient(180deg,#3e3e3e,#6a6a5c 40%,#8b8577)"></div>
<h2 class="abs display" style="left:635px;top:2671px;font-size:50px">Expert staff +<br><em>heavy duty</em><br>trucks</h2>
<p class="abs body-copy" style="left:635px;top:2850px;width:440px">Lorem Ipsum is simply dummy text of the printing and typesetting industry. Lorem Ipsum has been the industry's standard dummy text ever since the 1500s, when an unknown printer took a galley of type and scrambled it.</p>
<div class="btn green" style="left:635px;top:2987px;width:165px;height:36px">Call us today</div>

<!-- Testimonials -->
<div class="abs testimonials">
  <div class="abs brand" style="left:8px;top:40px;font-size:64px;color:#343232">Haulbright</div>
  <h2 class="abs display" style="left:0;top:92px;width:1200px;text-align:center;font-size:50px;color:var(--white)">We <em>love</em> our<br>valued customers!</h2>
  <div class="card" style="left:135px">
    <div class="avatar" role="img" aria-label="Customer portrait"></div>
    <div class="quote">“</div>
    <p>Lorem Ipsum is simply dummy text of the printing and typesetting industry. Lorem Ipsum has been the industry's standard dummy text ever since the 1500s, when an unknown</p>
    <div class="name">JOHN DOE</div><div class="role">Owner Of Lorem</div>
  </div>
  <div class="card" style="left:615px">
    <div class="avatar" role="img" aria-label="Customer portrait" style="background:linear-gradient(135deg,#e8e2de,#6d4e3e)"></div>
    <div class="quote">“</div>
    <p>Lorem Ipsum is simply dummy text of the printing and typesetting industry. Lorem Ipsum has been the industry's standard dummy text ever since the 1500s, when an unknown</p>
    <div class="name">JOHN DOE</div><div class="role">Owner Of Lorem</div>
  </div>
  <div class="arrow-btn" style="left:540px;top:512px;width:30px;height:30px;background:#fff"><svg width="16" height="10" viewBox="0 0 16 10"><path d="M16 5H2M6 1L2 5l4 4" stroke="#222" stroke-width="1.5" fill="none"/></svg></div>
  <div class="arrow-btn" style="left:614px;top:507px;width:40px;height:40px;background:#fff"><svg width="22" height="10" viewBox="0 0 22 10"><path d="M0 5h20M16 1l4 4-4 4" stroke="#4ea340" stroke-width="1.5" fill="none"/></svg></div>
</div>

<!-- Footer -->
<div class="abs" role="img" aria-label="Green dump truck" style="left:0;top:4020px;width:150px;height:160px;background:linear-gradient(135deg,#5fae3f,#2f6e24);border-radius:10px 30px 40px 10px"></div>
<div class="abs" role="img" aria-label="Green dump truck" style="left:1050px;top:4020px;width:150px;height:160px;background:linear-gradient(225deg,#5fae3f,#2f6e24);border-radius:30px 10px 10px 40px"></div>
<div class="abs brand" style="left:0;top:4090px;width:1200px;text-align:center;font-size:62px;line-height:1;color:var(--green)">Haulbright</div>
<div class="abs brand" style="left:0;top:4158px;width:1200px;text-align:center;font-size:36px;line-height:1">Junk Removal</div>

<div class="abs foot-col" style="left:135px;top:4258px;width:240px">
  <h3>About us</h3>
  <p class="body-copy" style="font-size:11.5px;line-height:23px;color:var(--ink)">Lorem Ipsum is simply dummy text of the printing and typesetting industry. Lorem Ipsum has been the industry's standard dummy text ever since the 1500s.</p>
  <div class="social"><span></span><span></span><span></span></div>
</div>
<div class="abs divider" style="left:449px;top:4278px"></div>
<div class="abs foot-col" style="left:526px;top:4262px">
  <h3>Quick links</h3>
  <ul class="foot-links"><li>Who We Are</li><li>What We Do</li><li>Jobs We Do</li><li>Our Work</li><li>Blog</li><li>Faqs</li></ul>
</div>
<div class="abs divider" style="left:772px;top:4278px"></div>
<div class="abs foot-col" style="left:850px;top:4262px;width:230px">
  <h3>Contact us</h3>
  <div class="contact-row"><span class="dot"><svg width="13" height="13" viewBox="0 0 24 24"><path fill="#fff" d="M6.6 10.8a15 15 0 006.6 6.6l2.2-2.2c.3-.3.7-.4 1-.2 1.1.4 2.3.6 3.6.6.6 0 1 .4 1 1V20c0 .6-.4 1-1 1A17 17 0 013 4c0-.6.4-1 1-1h3.5c.6 0 1 .4 1 1 0 1.3.2 2.5.6 3.6.1.3 0 .7-.2 1z"/></svg></span>+1 (555) 014-2290</div>
  <div class="contact-row"><span class="dot"><svg width="13" height="10" viewBox="0 0 24 18"><rect width="24" height="18" fill="#fff"/><path d="M1 1l11 8 11-8" stroke="#4ea340" stroke-width="2" fill="none"/></svg></span>lorem@ipsum.com</div>
  <div class="contact-row" style="line-height:16px"><span class="dot"><svg width="11" height="14" viewBox="0 0 20 26"><path fill="#fff" d="M10 0a10 10 0 00-10 10c0 7.5 10 16 10 16s10-8.5 10-16A10 10 0 0010 0zm0 14a4 4 0 110-8 4 4 0 010 8z"/></svg></span>Lorem Ipsum is simply dummy text of the printing</div>
</div>

<div class="abs" style="left:0;top:4545px;width:1200px;text-align:center;font-size:11px">© 2023 All Rights Reserved | Brightfield Web LLC D.B.A. <span style="font-family:'Bowlby One',sans-serif;color:var(--green)">Haulbright</span></div>

</body>
</html>
```